Australian Based Booking Platform Needs Playful Home Page & Profile Page To Showcase Our Acti...

COMPANY OVERVIEW:
WANDER-ON TICKETS is an Australian based activity booking platform. Our point of difference is our Kiosk machines that are located in hotels around Australia and allow customers instant access to book activities from the hotel reception.

HOME PAGE:
This page needs to clearly show that we are Australia’s leading booking platform.
Our Competition: https://www.roamplicity.com.au/en
IMPORTANT SECTIONS ON THE HOME PAGE:
- Key Bullet Points (Best Price Guaranteed, Trusted By Thousands, Australian Owned, Unbeatable Support)
- Top Experiences – (Images of selected experiences in a slider format)
- Take Me There – Gold Coast, Carins, Port Duglas, Sunshine Coast, Whitsundays, Brisbane, Sydney, Adelaide, Hobart, Perth
- Top Deals For You – (Images of selected experiences in a slider format)
- Experiences You’ll Love – (Categories of Adventure Tours, Outdoor Activities, Hot Deals, Fun & Games, Zoos & Aquariums, Reef & Island Cruises)
- Testimonials – (some sort of slider format)
- Top New Experience – (Images of selected experiences in a slider format)
- Footer Menu
NOTE: Including some sort of mascot on the page to introduce a personality would be amazing. A Kangaroo or Koala could be a good choice.

REGION PAGE:
This page needs to clearly show what is on offer in the region. The layout of this page will be used for all regions in Australia (eg Gold Coast, Carins, Port Duglas, Sunshine Coast, Whitsundays, Brisbane, Sydney, Adelaide, Hobart, Perth)
IMPORTANT SECTIONS ON THE REGION PAGE:
- Categories: Adventure Tours, Outdoor Activities, Hot Deals, Fun & Games, Zoos & Aquariums, Reef & Island Cruises
o This Categories menu allows you to flick between sliders with activities from the different categories
- Footer Menu

PROFILE PAGE:
The layout of this page is going to be used to clearly show off every activity people can book.
Competitors Example:
https://www.trekvane.com/tours/Sydney/Sydney-Harbour-Northern-beaches-and-National-Park/d482-559213K7
https://www.roamplicity.com.au/en/gold-coast/bellwick-isle-seal-and-corvana-reefs-snorkelling-cruise
IMPORTANT SECTIONS ON THE PROFILE PAGE:
- Tour Title
- Photos / Video
- Booking Calanda (As displayed on the above link)
- Highlights & Inclusions
- Overview
- Location (Map)
- What To Bring
- Additional Information
- Booking Information
- Reviews:
- Terms & Conditions
NOTE: This page is to be displayed on a kiosk with the following dimensions;
- 1209.8mm x 680.4mm
- Aspect Ratio 16:9

I have uploaded some images of Australia, as well as our logo. Please feel free to use or not use these images as you decide.
Updates

Keep up the good work on the designs :)

Target Market(s)

Australian Holiday Makers

Industry/Entity Type

Tourism Booking Platform

Number of Pages Required

3 page

Font styles to use
Sans Serif

Requirements
Must have
• - This booking calendar https://app.clipvault.com/kR7tWmZ2Lpq9
Nice to have
• A mascot or something to add character to the page.

```html
<!DOCTYPE html>
<html lang="en">
<head>
<meta charset="utf-8">
<title>Wander-On Tickets – Home</title>
<link href="https://fonts.googleapis.com/css2?family=Poppins:wght@400;500;600;700&family=Russo+One&display=swap" rel="stylesheet">
<style>
:root{
  --stage:#fbeed3;
  --yellow:#f9c11a;
  --amber:#fdb94a;
  --cream:#fff7e4;
  --red:#e23b2e;
  --ink:#1f1f1f;
  --muted:#8a8a8a;
  --line:#ececec;
  --white:#ffffff;
  --dark:#111111;
}
*{box-sizing:border-box;margin:0;padding:0}
html,body{width:1200px;height:2925px;overflow:hidden}
body{background:var(--stage);font-family:"Poppins",sans-serif;color:var(--ink);position:relative}
.screen{position:absolute;background:var(--white);overflow:hidden;border-radius:10px}
.screen--preview{left:152px;top:70px;width:646px;height:435px}
.screen--mobile{left:861px;top:70px;width:191px;height:2654px;border-radius:14px}
.screen--page{left:152px;top:548px;width:646px;height:2307px}

.site-header{height:39px;display:flex;align-items:center;justify-content:space-between;padding:0 48px 0 67px;background:var(--white)}
.brand{display:flex;align-items:center;gap:5px;font-weight:700;font-size:11px;letter-spacing:.5px;color:var(--ink);white-space:nowrap}
.brand__dot{width:9px;height:9px;border-radius:50%;background:var(--yellow)}
.nav{display:flex;align-items:center;gap:16px;font-size:6.5px;color:#333}
.nav__hot::before{content:"";display:inline-block;width:4px;height:5px;border-radius:50% 50% 50% 0;background:#f08a1c;margin-right:2px}
.btn-login{background:#eee;border-radius:10px;padding:3px 12px;font-size:6.5px;color:#555}
.icon-btn{width:14px;height:14px;border-radius:50%;border:1px solid var(--yellow)}

.hero{position:relative;height:225px;background:var(--amber)}
.hero__photo{position:absolute;left:169px;right:0;top:0;bottom:0;background:linear-gradient(180deg,#b7d6ef 0%,#cfe2ee 28%,#3c87a8 45%,#1f6c88 70%,#5f8f4f 100%)}
.hero__copy{position:absolute;left:67px;top:58px;z-index:2}
.hero__title{font-family:"Russo One",sans-serif;color:var(--white);font-size:21px;line-height:27px;letter-spacing:.5px}
.arrows{display:flex;gap:4px;margin-top:12px}
.arrow{width:25px;height:11px;border-radius:6px;display:flex;align-items:center;justify-content:center}
.arrow--prev{background:#f6e0b6}
.arrow--next{background:var(--dark)}
.arrow svg{width:10px;height:6px}

.features{height:62px;display:flex;justify-content:center;gap:38px;align-items:center}
.feature{display:flex;align-items:center;gap:7px;font-size:6px;font-weight:500;line-height:8px;text-transform:uppercase;color:#333}
.feature__icon{width:22px;height:22px;border-radius:50%;background:#fff4d6;display:flex;align-items:center;justify-content:center}
.feature__icon svg{width:12px;height:12px}

.section{position:relative;text-align:center}
.section--cream{background:var(--cream)}
.section__title{font-weight:700;font-size:13px;letter-spacing:.4px;text-transform:uppercase;color:var(--ink)}
.tabs{display:flex;justify-content:center;gap:6px;margin-top:12px}
.tab{font-size:5.5px;padding:3px 9px;border-radius:8px;background:#f2f2f2;color:#444}
.tab--active{background:var(--yellow);color:var(--ink)}

.cards{display:flex;gap:17px;position:absolute;left:96px}
.card{width:140px;height:181px;background:var(--white);border-radius:4px;box-shadow:0 1px 5px rgba(0,0,0,.12);text-align:left;overflow:hidden}
.card__img{height:90px;margin:3px;border-radius:3px}
.card__body{padding:4px 9px}
.badges{display:flex;gap:3px}
.badge{font-size:4.5px;color:var(--white);padding:1px 4px;border-radius:2px}
.badge--hot{background:var(--red)}
.badge--best{background:#f0a51a}
.card__by{font-size:4.5px;color:var(--muted);margin-top:7px}
.card__title{font-size:6px;font-weight:600;line-height:8px;margin-top:3px}
.card__foot{display:flex;justify-content:space-between;align-items:flex-end;margin-top:13px}
.from{display:block;font-size:4.5px;color:var(--muted)}
.old{font-size:6.5px;color:var(--red);font-weight:600;margin-right:8px}
.price{font-size:6.5px;font-weight:600}
.rating{font-size:5px;border:1px solid var(--line);border-radius:4px;padding:1px 4px;color:#555}
.progress{position:absolute;left:96px;width:454px;height:3px;border-radius:2px;background:#eee}
.progress__fill{position:absolute;left:20px;width:210px;height:3px;border-radius:2px;background:var(--yellow)}

.mascot{position:absolute;border-radius:48% 52% 40% 40%;background:linear-gradient(160deg,#f2a03d,#d9782a)}
.mascot--koala{background:linear-gradient(160deg,#b9bcc2,#8a8f98)}

.places{position:absolute;left:67px;top:70px;display:flex;gap:12px}
.place{width:93px;text-align:center;font-size:6.5px;font-weight:500}
.place__img{height:125px;border-radius:46px;margin-bottom:6px;position:relative}
.place__img--active{display:flex;align-items:center;justify-content:center}
.plus{width:22px;height:22px;border-radius:50%;background:var(--yellow);display:flex;align-items:center;justify-content:center;color:var(--white);font-size:14px;line-height:1}

.cats{position:absolute;left:96px;top:70px;display:grid;grid-template-columns:repeat(3,140px);gap:17px 17px}
.cat{background:var(--white);border-radius:4px;box-shadow:0 1px 5px rgba(0,0,0,.1);overflow:hidden}
.cat__img{height:89px;margin:3px;border-radius:3px;display:flex;align-items:center;justify-content:center}
.cat__label{font-size:6px;font-weight:600;padding:5px 0 7px}
.cat--active{background:var(--yellow)}

.reviews-title{position:absolute;left:96px;top:62px;text-align:left;font-weight:700;font-size:12.5px;line-height:16px;text-transform:uppercase}
.review{position:absolute;width:142px;height:130px;background:var(--white);border-radius:4px;box-shadow:0 1px 5px rgba(0,0,0,.1);text-align:left;padding:8px 10px}
.quote{font-family:"Russo One",sans-serif;color:var(--yellow);font-size:16px;line-height:12px}
.stars{color:#d8d8d8;font-size:6px;letter-spacing:1px;margin-top:2px}
.review p{font-size:5px;line-height:7px;color:#333;margin-top:6px}
.reviewer{display:flex;gap:5px;align-items:center;margin-top:14px}
.avatar{width:18px;height:18px;border-radius:50%;background:#e3c9a4;border:1px solid var(--yellow)}
.reviewer__name{font-size:5px;color:#e8a21a;font-weight:600}
.reviewer__place{font-size:4.5px;color:var(--muted)}

.footer{position:relative;height:193px;background:var(--white);text-align:left}
.footer__brand{position:absolute;left:67px;top:28px;width:170px}
.footer__about{font-size:5px;line-height:7px;color:#555;margin-top:14px}
.footer__label{font-size:5.5px;font-weight:700;margin-top:12px;text-transform:uppercase}
.newsletter{display:flex;align-items:center;margin-top:6px;border:1px solid var(--line);border-radius:9px;height:17px;padding-left:8px;width:170px;justify-content:space-between}
.newsletter span{font-size:5px;color:#bbb}
.newsletter .btn-sub{color:var(--ink)}
.btn-sub{background:var(--yellow);border-radius:9px;font-size:5.5px;font-weight:600;padding:4px 9px;white-space:nowrap}
.footer__col{position:absolute;top:28px;font-size:5px;line-height:7.4px;color:#777}
.footer__col h4{font-size:5.5px;color:var(--ink);font-weight:700;margin-bottom:4px;text-transform:uppercase}
.footer__col .hl{color:#e8a21a}
.bottom-bar{height:17px;background:var(--dark);color:var(--white);font-size:5px;display:flex;align-items:center;justify-content:space-between;padding:0 67px}
.socials{display:flex;gap:3px}
.social{width:9px;height:9px;border-radius:50%;background:var(--white)}
.social--on{background:var(--yellow)}

.booking-tab{position:absolute;right:0;background:var(--yellow);border-radius:6px 0 0 6px;display:flex;align-items:center;gap:4px;padding:4px 6px;font-size:5px;font-weight:700;line-height:6px}
.booking-tab i{width:11px;height:11px;border-radius:3px;background:var(--white)}

.m-header{height:48px;display:flex;align-items:center;justify-content:space-between;padding:0 8px}
.m-header .brand{font-size:7.5px;gap:3px}
.m-header .brand__dot{width:7px;height:7px}
.m-actions{display:flex;gap:3px;align-items:center}
.m-actions .btn-login{font-size:5.5px;padding:2px 6px}
.m-actions .icon-btn{width:11px;height:11px}
.menu-btn{width:13px;height:13px;border-radius:50%;background:var(--dark)}
.m-hero{height:211px;position:relative}
.m-hero__photo{height:130px;background:linear-gradient(180deg,#b7d6ef 0%,#d2e4ee 35%,#3c87a8 55%,#1f6c88 80%,#5f8f4f 100%)}
.m-hero__panel{position:absolute;left:6px;right:6px;top:130px;height:81px;background:var(--amber);text-align:center;padding-top:14px}
.m-hero__panel .hero__title{font-size:12.5px;line-height:17px}
.m-hero__panel .arrows{justify-content:center;margin-top:6px}
.m-features{height:91px;display:flex;justify-content:space-around;padding:20px 4px 0;text-align:center}
.m-feature{font-size:5.5px;line-height:7px;text-transform:uppercase;font-weight:500;width:56px}
.m-feature .feature__icon{margin:0 auto 5px;width:26px;height:26px}
.m-section{position:relative;text-align:center;overflow:hidden}
.m-section .section__title{font-size:10px;padding-top:14px}
.m-tabs{display:flex;gap:5px;padding-left:6px;margin-top:12px}
.m-tabs .tab{font-size:6px;padding:3px 10px}
.m-cards{position:absolute;left:6px;display:flex;gap:8px}
.m-card{width:155px;height:200px}
.m-card .card__img{height:92px}
.m-card .card__by{font-size:5.5px;margin-top:8px}
.m-card .card__title{font-size:6.5px;line-height:9px}
.m-card .badge{font-size:5.5px}
.m-card .old,.m-card .price{font-size:7.5px}
.m-card .card__foot{margin-top:14px}
.m-progress{position:absolute;left:6px;width:160px;height:3px;background:#eee;border-radius:2px}
.m-progress i{position:absolute;left:0;width:64px;height:3px;background:var(--yellow);border-radius:2px}
.m-places{position:absolute;left:6px;top:48px;display:flex;gap:9px}
.m-place{width:73px;font-size:7px;font-weight:500}
.m-place .place__img{height:97px;border-radius:36px}
.m-cats{display:grid;grid-template-columns:85px 85px;gap:10px 8px;padding:10px 6px 0}
.m-cats .cat__img{height:68px}
.m-cats .cat__label{font-size:6.5px;line-height:8px;padding:4px 0 5px}
.m-reviews{position:absolute;left:16px;top:70px;display:flex;gap:12px}
.m-review{position:relative;width:148px;height:160px}
.m-review p{font-size:6.5px;line-height:9px}
.m-footer{height:465px;text-align:center;padding-top:40px}
.m-footer .brand{justify-content:center;font-size:10px}
.m-footer .footer__label{margin-top:24px;font-size:7px}
.m-newsletter{margin:8px auto 0;width:175px;height:22px;border:1px solid var(--line);border-radius:11px;font-size:6px;color:#bbb;text-align:left;padding:5px 10px}
.m-footer .btn-sub{display:inline-block;margin-top:10px;font-size:6.5px;padding:5px 14px}
.accordion{margin-top:22px;text-align:left;padding:0 6px}
.acc{display:flex;justify-content:space-between;align-items:center;font-size:7px;font-weight:700;text-transform:uppercase;padding:7px 0;border-bottom:1px solid var(--line)}
.acc i{width:10px;height:10px;border-radius:50%;border:1px solid #ccc}
.acc--open i{background:var(--yellow);border-color:var(--yellow)}
.acc-list{font-size:6.5px;line-height:12px;color:#777;padding:4px 0 6px}
.acc-list .hl{color:#e8a21a;text-decoration:underline}
.m-bottom{height:34px;background:var(--dark);color:var(--white);font-size:6.5px;text-align:center;padding-top:5px}
.m-bottom .socials{justify-content:center;margin-bottom:4px}
.m-bottom .social{width:11px;height:11px}
</style>
</head>
<body>

<section class="screen screen--preview" aria-label="Home page, first screen">
  <header class="site-header" style="padding-left:40px">
    <div class="brand"><span class="brand__dot"></span>WANDER-ON TICKETS</div>
    <nav class="nav"><span>Destinations</span><span>Experiences</span><span class="nav__hot">Hot Deals</span><span>Gifts</span><span class="btn-login">Login</span><span class="icon-btn"></span><span class="icon-btn"></span></nav>
  </header>
  <div class="hero" style="height:250px">
    <div class="hero__photo" style="left:152px" role="img" aria-label="Aerial photo of a harbour city with bridge and parkland"></div>
    <div class="hero__copy" style="left:40px;top:65px">
      <h1 class="hero__title" style="font-size:25px;line-height:30px">DISCOVER THE<br>MOST ENGAGING<br>PLACES</h1>
      <div class="arrows"><span class="arrow arrow--prev"><svg viewBox="0 0 10 6"><path d="M9 3H1M3 1L1 3l2 2" stroke="#a88" fill="none"/></svg></span><span class="arrow arrow--next"><svg viewBox="0 0 10 6"><path d="M1 3h8M7 1l2 2-2 2" stroke="#fff" fill="none"/></svg></span></div>
    </div>
  </div>
  <div class="features" style="height:74px">
    <div class="feature"><span class="feature__icon"><svg viewBox="0 0 12 12"><circle cx="6" cy="5" r="3.5" fill="none" stroke="#f9c11a"/><path d="M4 8l-1 3 3-1 3 1-1-3" fill="none" stroke="#f9c11a"/></svg></span>Best price<br>guaranteed</div>
    <div class="feature"><span class="feature__icon"><svg viewBox="0 0 12 12"><path d="M1 6l3-3 2 2 2-2 3 3-5 4z" fill="none" stroke="#f9c11a"/></svg></span>Trusted by<br>thousands</div>
    <div class="feature"><span class="feature__icon"><svg viewBox="0 0 12 12"><path d="M6 11s4-4 4-6.5a4 4 0 0 0-8 0C2 7 6 11 6 11z" fill="none" stroke="#f9c11a"/></svg></span>Australian<br>owned</div>
    <div class="feature"><span class="feature__icon"><svg viewBox="0 0 12 12"><path d="M2 7V6a4 4 0 0 1 8 0v1M2 7h2v3H2zM8 7h2v3H8z" fill="none" stroke="#f9c11a"/></svg></span>Unbeatable<br>support</div>
  </div>
  <div class="booking-tab" style="top:333px;padding:6px 4px"><i></i></div>
  <div class="section">
    <h2 class="section__title">Top Experiences</h2>
    <div class="tabs"><span class="tab tab--active">Gold Coast</span><span class="tab">Cairns</span><span class="tab">Sydney</span><span class="tab">Queenstown</span><span class="tab">Melbourne</span><span class="tab">Tasmania</span><span class="tab">Port Douglas</span></div>
  </div>
</section>

<section class="screen screen--mobile" aria-label="Home page, mobile">
  <header class="m-header">
    <div class="brand"><span class="brand__dot"></span>WANDER-ON</div>
    <div class="m-actions"><span class="btn-login">Login</span><span class="icon-btn"></span><span class="icon-btn"></span><span class="menu-btn"></span></div>
  </header>
  <div class="m-hero">
    <div class="m-hero__photo" role="img" aria-label="Aerial photo of a harbour city"></div>
    <div class="m-hero__panel">
      <h1 class="hero__title">DISCOVER THE MOST<br>ENGAGING PLACES</h1>
      <div class="arrows"><span class="arrow arrow--prev"><svg viewBox="0 0 10 6"><path d="M9 3H1M3 1L1 3l2 2" stroke="#a88" fill="none"/></svg></span><span class="arrow arrow--next"><svg viewBox="0 0 10 6"><path d="M1 3h8M7 1l2 2-2 2" stroke="#fff" fill="none"/></svg></span></div>
    </div>
  </div>
  <div class="m-features">
    <div class="m-feature"><div class="feature__icon"><svg viewBox="0 0 12 12"><circle cx="6" cy="5" r="3.5" fill="none" stroke="#f9c11a"/></svg></div>Best price guaranteed</div>
    <div class="m-feature"><div class="feature__icon"><svg viewBox="0 0 12 12"><path d="M1 6l3-3 2 2 2-2 3 3-5 4z" fill="none" stroke="#f9c11a"/></svg></div>Trusted by thousands</div>
    <div class="m-feature"><div class="feature__icon"><svg viewBox="0 0 12 12"><path d="M6 11s4-4 4-6.5a4 4 0 0 0-8 0C2 7 6 11 6 11z" fill="none" stroke="#f9c11a"/></svg></div>Australian owned</div>
  </div>
  <div class="m-section" style="height:318px">
    <h2 class="section__title" style="padding-top:8px">Top Experiences</h2>
    <div class="m-tabs"><span class="tab tab--active">Gold Coast</span><span class="tab">Cairns</span><span class="tab">Sydney</span><span class="tab">Qu</span></div>
    <div class="m-cards" style="top:62px">
      <div class="card m-card"><div class="card__img" style="background:linear-gradient(160deg,#6aa4d8,#3c6fa8 60%,#9bbf6a)" role="img" aria-label="Theme park visitors on rides"></div><div class="card__body"><div class="badges"><span class="badge badge--hot">Hot deal</span><span class="badge badge--best">Best seller</span></div><p class="card__by">by Zestoria Tickets</p><p class="card__title">Zestoria Park, Wavelark World &amp; Loftpeak 3 Day Ticket</p><div class="card__foot"><div><span class="from">from</span><span class="old">$159.00</span><span class="price">$141.55</span></div><span class="rating">★ 4.7</span></div></div></div>
      <div class="card m-card"><div class="card__img" style="background:linear-gradient(160deg,#6aa4d8,#3c6fa8)" role="img" aria-label="Theme park photo"></div></div>
    </div>
    <div class="m-progress" style="top:304px"><i></i></div>
  </div>
  <div class="m-section section--cream" style="height:227px">
    <div class="mascot" style="right:14px;top:-18px;width:24px;height:34px" role="img" aria-label="Kangaroo mascot"></div>
    <h2 class="section__title" style="padding-top:28px">Take Me There</h2>
    <div class="m-places">
      <div class="m-place"><div class="place__img" style="background:linear-gradient(160deg,#4aa3e0,#f0b52a 60%,#e2e8ef)" role="img" aria-label="Roller coaster against the sky"></div>Gold Coast</div>
      <div class="m-place"><div class="place__img" style="background:linear-gradient(180deg,#2f7fc4,#15477f)" role="img" aria-label="Scuba divers underwater"></div>Carins</div>
      <div class="m-place"><div class="place__img" style="background:linear-gradient(180deg,#8ec8e8,#2f8db7)" role="img" aria-label="Island jetty"></div>Po</div>
    </div>
    <div class="m-progress" style="top:188px"><i></i></div>
  </div>
  <div class="m-section" style="height:295px">
    <h2 class="section__title" style="padding-top:30px">Top Deals For You</h2>
    <div class="m-cards" style="top:56px">
      <div class="card m-card"><div class="card__img" style="background:linear-gradient(180deg,#7fb6e6,#cfd9e2 55%,#3a7cc0)" role="img" aria-label="Surf lesson on the beach"></div><div class="card__body"><div class="badges"><span class="badge badge--hot">Hot deal</span><span class="badge badge--best">Best seller</span></div><p class="card__by">by Zestoria Tickets</p><p class="card__title">Zestoria Park, Wavelark World &amp; Loftpeak 3 Day Ticket</p><div class="card__foot"><div><span class="from">from</span><span class="old">$159.00</span><span class="price">$141.55</span></div><span class="rating">★ 4.7</span></div></div></div>
      <div class="card m-card"><div class="card__img" style="background:linear-gradient(160deg,#7fb6e6,#3a7cc0)" role="img" aria-label="Beach activity photo"></div></div>
    </div>
    <div class="mascot" style="left:8px;top:262px;width:26px;height:30px" role="img" aria-label="Kangaroo mascot"></div>
  </div>
  <div class="m-section section--cream" style="height:420px">
    <h2 class="section__title" style="padding-top:20px">Experiences You'll Love</h2>
    <div class="m-cats">
      <div class="cat"><div class="cat__img" style="background:linear-gradient(180deg,#24345f,#e0664a)" role="img" aria-label="Ferris wheel at dusk"></div><div class="cat__label">Categories of<br>Adventure Tours</div></div>
      <div class="cat"><div class="cat__img" style="background:linear-gradient(180deg,#4e7a3c,#2c4a23)" role="img" aria-label="Hikers in a forest"></div><div class="cat__label">Outdoor<br>Activities</div></div>
      <div class="cat cat--active"><div class="cat__img" style="background:linear-gradient(160deg,#e7b464,#c88a3a)" role="img" aria-label="Map with a travel pin"><span class="plus">+</span></div><div class="cat__label">Hot Deals<br>&nbsp;</div></div>
      <div class="cat"><div class="cat__img" style="background:linear-gradient(160deg,#3b4f8f,#d98d5b)" role="img" aria-label="Friends at an arcade"></div><div class="cat__label">Fun &amp; Games<br>&nbsp;</div></div>
      <div class="cat"><div class="cat__img" style="background:linear-gradient(180deg,#2d6f84,#16404f)" role="img" aria-label="Aquarium tunnel"></div><div class="cat__label">Zoos &amp;<br>Aquariums</div></div>
      <div class="cat"><div class="cat__img" style="background:linear-gradient(180deg,#8ab8dd,#e9eef3 55%,#2b6f9c)" role="img" aria-label="Cruise ship at sea"></div><div class="cat__label">Reef &amp; Island<br>Cruises</div></div>
    </div>
    <div class="mascot mascot--koala" style="right:4px;top:392px;width:30px;height:22px" role="img" aria-label="Koala mascot on a branch"></div>
  </div>
  <div class="m-section" style="height:261px">
    <h2 class="section__title" style="padding-top:34px;line-height:13px">What Our Travelers<br>Are Saying</h2>
    <div class="m-reviews">
      <div class="review m-review"><div class="quote">“</div><div class="stars">★★★★★</div><p>Lorem Ipsum is simply dummy text of the printing and typesetting industry. Lorem Ipsum has been the industry's standard dummy text ever...</p><div class="reviewer"><span class="avatar"></span><div><div class="reviewer__name">Marla Denholm</div><div class="reviewer__place">New York, USA</div></div></div></div>
      <div class="review m-review"><div class="quote">“</div></div>
    </div>
  </div>
  <div class="m-section" style="height:284px">
    <h2 class="section__title" style="padding-top:30px">Top New Experience</h2>
    <div class="m-cards" style="top:56px">
      <div class="card m-card"><div class="card__img" style="background:linear-gradient(160deg,#f3b15a,#c2552f 55%,#5c7a2f)" role="img" aria-label="Couple watching hot air balloons"></div><div class="card__body"><div class="badges"><span class="badge badge--hot">Hot deal</span><span class="badge badge--best">Best seller</span></div><p class="card__by">by Zestoria Tickets</p><p class="card__title">Zestoria Park, Wavelark World &amp; Loftpeak 3 Day Ticket</p><div class="card__foot"><div><span class="from">from</span><span class="old">$159.00</span><span class="price">$141.55</span></div><span class="rating">★ 4.7</span></div></div></div>
      <div class="card m-card"><div class="card__img" style="background:linear-gradient(160deg,#f3b15a,#c2552f)" role="img" aria-label="Balloon ride photo"></div></div>
    </div>
    <div class="m-progress" style="top:268px"><i></i></div>
  </div>
  <footer class="m-footer" style="position:relative">
    <div class="mascot" style="left:8px;top:-6px;width:26px;height:30px" role="img" aria-label="Kangaroo mascot"></div>
    <div class="brand"><span class="brand__dot"></span>WANDER-ON TICKETS</div>
    <div class="footer__label">Sign up for our newsletter</div>
    <div class="m-newsletter">hello@wanderon-mail.com</div>
    <span class="btn-sub">SUBSCRIBE →</span>
    <div class="accordion">
      <div class="acc">Top Destinations<i></i></div>
      <div class="acc">Popular Cities<i></i></div>
      <div class="acc acc--open" style="border-bottom:0">Our Company<i></i></div>
      <div class="acc-list"><span class="hl">About Us</span><br>FAQs<br>Blogs<br>Privacy Policy<br>Terms and Conditions<br>Security</div>
      <div class="acc">Join Us<i></i></div>
    </div>
    <div class="booking-tab" style="top:432px"><i></i>BOOKING<br>CALENDAR</div>
  </footer>
  <div class="m-bottom">
    <div class="socials"><span class="social"></span><span class="social social--on"></span><span class="social"></span><span class="social"></span></div>
    © 2023 Wander-On. All Right Reserved
  </div>
</section>

<section class="screen screen--page" aria-label="Home page, desktop">
  <header class="site-header">
    <div class="brand"><span class="brand__dot"></span>WANDER-ON TICKETS</div>
    <nav class="nav"><span>Destinations</span><span>Experiences</span><span class="nav__hot">Hot Deals</span><span>Gifts</span><span class="btn-login">Login</span><span class="icon-btn"></span><span class="icon-btn"></span></nav>
  </header>
  <div class="hero">
    <div class="hero__photo" role="img" aria-label="Aerial photo of a harbour city with bridge and parkland"></div>
    <div class="hero__copy">
      <h1 class="hero__title">DISCOVER THE<br>MOST ENGAGING<br>PLACES</h1>
      <div class="arrows"><span class="arrow arrow--prev"><svg viewBox="0 0 10 6"><path d="M9 3H1M3 1L1 3l2 2" stroke="#a88" fill="none"/></svg></span><span class="arrow arrow--next"><svg viewBox="0 0 10 6"><path d="M1 3h8M7 1l2 2-2 2" stroke="#fff" fill="none"/></svg></span></div>
    </div>
  </div>
  <div class="features">
    <div class="feature"><span class="feature__icon"><svg viewBox="0 0 12 12"><circle cx="6" cy="5" r="3.5" fill="none" stroke="#f9c11a"/><path d="M4 8l-1 3 3-1 3 1-1-3" fill="none" stroke="#f9c11a"/></svg></span>Best price<br>guaranteed</div>
    <div class="feature"><span class="feature__icon"><svg viewBox="0 0 12 12"><path d="M1 6l3-3 2 2 2-2 3 3-5 4z" fill="none" stroke="#f9c11a"/></svg></span>Trusted by<br>thousands</div>
    <div class="feature"><span class="feature__icon"><svg viewBox="0 0 12 12"><path d="M6 11s4-4 4-6.5a4 4 0 0 0-8 0C2 7 6 11 6 11z" fill="none" stroke="#f9c11a"/></svg></span>Australian<br>owned</div>
    <div class="feature"><span class="feature__icon"><svg viewBox="0 0 12 12"><path d="M2 7V6a4 4 0 0 1 8 0v1M2 7h2v3H2zM8 7h2v3H8z" fill="none" stroke="#f9c11a"/></svg></span>Unbeatable<br>support</div>
  </div>
  <div class="booking-tab" style="top:276px"><i></i>BOOKING<br>CALENDAR</div>

  <section class="section" style="height:306px">
    <h2 class="section__title" style="padding-top:12px">Top Experiences</h2>
    <div class="tabs"><span class="tab tab--active">Gold Coast</span><span class="tab">Cairns</span><span class="tab">Sydney</span><span class="tab">Queenstown</span><span class="tab">Melbourne</span><span class="tab">Tasmania</span><span class="tab">Port Douglas</span></div>
    <div class="cards" style="top:70px">
      <div class="card"><div class="card__img" style="background:linear-gradient(160deg,#6aa4d8,#3c6fa8 60%,#9bbf6a)" role="img" aria-label="Theme park visitors on rides"></div><div class="card__body"><div class="badges"><span class="badge badge--hot">Hot deal</span><span class="badge badge--best">Best seller</span></div><p class="card__by">by Zestoria Tickets</p><p class="card__title">Zestoria Park, Wavelark World &amp;<br>Loftpeak 3 Day Ticket</p><div class="card__foot"><div><span class="from">from</span><span class="old">$159.00</span><span class="price">$141.55</span></div><span class="rating">★ 4.7</span></div></div></div>
      <div class="card"><div class="card__img" style="background:linear-gradient(160deg,#f3b15a,#c2552f 55%,#5c7a2f)" role="img" aria-label="Couple watching hot air balloons"></div><div class="card__body"><div class="badges"><span class="badge badge--hot">Hot deal</span><span class="badge badge--best">Best seller</span></div><p class="card__by">by Zestoria Tickets</p><p class="card__title">Zestoria Park, Wavelark World &amp;<br>Loftpeak 3 Day Ticket</p><div class="card__foot"><div><span class="from">from</span><span class="old">$159.00</span><span class="price">$141.55</span></div><span class="rating">★ 4.7</span></div></div></div>
      <div class="card"><div class="card__img" style="background:linear-gradient(160deg,#4f9a3c,#e0b52c 45%,#c8402f 70%,#3d79b8)" role="img" aria-label="Colourful lorikeets feeding"></div><div class="card__body"><div class="badges"><span class="badge badge--hot">Hot deal</span><span class="badge badge--best">Best seller</span></div><p class="card__by">by Zestoria Tickets</p><p class="card__title">Zestoria Park, Wavelark World &amp;<br>Loftpeak 3 Day Ticket</p><div class="card__foot"><div><span class="from">from</span><span class="old">$159.00</span><span class="price">$141.55</span></div><span class="rating">★ 4.7</span></div></div></div>
    </div>
    <div class="progress" style="top:262px"><span class="progress__fill"></span></div>
    <div class="mascot" style="left:582px;top:200px;width:40px;height:70px" role="img" aria-label="Kangaroo mascot"></div>
  </section>

  <section class="section section--cream" style="height:276px;overflow:hidden">
    <h2 class="section__title" style="padding-top:38px">Take Me There</h2>
    <div class="places">
      <div class="place"><div class="place__img" style="background:linear-gradient(160deg,#4aa3e0,#f0b52a 60%,#e2e8ef)" role="img" aria-label="Roller coaster against the sky"></div>Gold Coast</div>
      <div class="place"><div class="place__img" style="background:linear-gradient(180deg,#2f7fc4,#15477f)" role="img" aria-label="Scuba divers underwater"></div>Carins</div>
      <div class="place"><div class="place__img" style="background:linear-gradient(180deg,#8ec8e8,#2f8db7)" role="img" aria-label="Island jetty in turquoise water"></div>Port Duglas</div>
      <div class="place"><div class="place__img place__img--active" style="background:linear-gradient(180deg,#3a3a30,#1e1e18)" role="img" aria-label="Sunshine Coast photo, darkened"><span class="plus">+</span></div>Sunshine Coast</div>
      <div class="place"><div class="place__img" style="background:linear-gradient(180deg,#6fb4de,#2e9aa8 60%,#6f9a4a)" role="img" aria-label="Aerial view of islands"></div>Whitsundays</div>
      <div class="place"><div class="place__img" style="background:linear-gradient(180deg,#f1a37a,#7d8fb4)" role="img" aria-label="Harbour at sunset"></div>Sydney</div>
    </div>
    <div class="mascot" style="left:2px;top:190px;width:56px;height:72px" role="img" aria-label="Kangaroo mascot"></div>
    <div class="progress" style="top:230px"><span class="progress__fill" style="left:10px;width:260px"></span></div>
  </section>

  <section class="section" style="height:314px">
    <h2 class="section__title" style="padding-top:44px">Top Deals For You</h2>
    <div class="mascot mascot--koala" style="left:550px;top:30px;width:60px;height:40px" role="img" aria-label="Koala mascot on a branch"></div>
    <div class="cards" style="top:70px">
      <div class="card"><div class="card__img" style="background:linear-gradient(180deg,#7fb6e6,#cfd9e2 55%,#3a7cc0)" role="img" aria-label="Surf lesson on the beach"></div><div class="card__body"><div class="badges"><span class="badge badge--hot">Hot deal</span><span class="badge badge--best">Best seller</span></div><p class="card__by">by Zestoria Tickets</p><p class="card__title">Zestoria Park, Wavelark World &amp;<br>Loftpeak 3 Day Ticket</p><div class="card__foot"><div><span class="from">from</span><span class="old">$159.00</span><span class="price">$141.55</span></div><span class="rating">★ 4.7</span></div></div></div>
      <div class="card"><div class="card__img" style="background:linear-gradient(160deg,#f3b15a,#c2552f 55%,#5c7a2f)" role="img" aria-label="Couple watching hot air balloons"></div><div class="card__body"><div class="badges"><span class="badge badge--hot">Hot deal</span><span class="badge badge--best">Best seller</span></div><p class="card__by">by Zestoria Tickets</p><p class="card__title">Zestoria Park, Wavelark World &amp;<br>Loftpeak 3 Day Ticket</p><div class="card__foot"><div><span class="from">from</span><span class="old">$159.00</span><span class="price">$141.55</span></div><span class="rating">★ 4.7</span></div></div></div>
      <div class="card"><div class="card__img" style="background:linear-gradient(160deg,#4f9a3c,#e0b52c 45%,#c8402f 70%,#3d79b8)" role="img" aria-label="Colourful lorikeets feeding"></div><div class="card__body"><div class="badges"><span class="badge badge--hot">Hot deal</span><span class="badge badge--best">Best seller</span></div><p class="card__by">by Zestoria Tickets</p><p class="card__title">Zestoria Park, Wavelark World &amp;<br>Loftpeak 3 Day Ticket</p><div class="card__foot"><div><span class="from">from</span><span class="old">$159.00</span><span class="price">$141.55</span></div><span class="rating">★ 4.7</span></div></div></div>
    </div>
    <div class="progress" style="top:268px"><span class="progress__fill"></span></div>
  </section>

  <section class="section section--cream" style="height:350px">
    <h2 class="section__title" style="padding-top:40px">Experiences You'll Love</h2>
    <div class="cats">
      <div class="cat"><div class="cat__img" style="background:linear-gradient(180deg,#24345f,#e0664a)" role="img" aria-label="Ferris wheel at dusk"></div><div class="cat__label">Categories of Adventure Tours</div></div>
      <div class="cat"><div class="cat__img" style="background:linear-gradient(180deg,#4e7a3c,#2c4a23)" role="img" aria-label="Hikers in a forest"></div><div class="cat__label">Outdoor Activities</div></div>
      <div class="cat"><div class="cat__img" style="background:linear-gradient(160deg,#e7b464,#c88a3a)" role="img" aria-label="Old map with a travel pin"></div><div class="cat__label">Hot Deals</div></div>
      <div class="cat"><div class="cat__img" style="background:linear-gradient(160deg,#3b4f8f,#d98d5b)" role="img" aria-label="Friends at an arcade"></div><div class="cat__label">Fun &amp; Games</div></div>
      <div class="cat"><div class="cat__img" style="background:linear-gradient(180deg,#2d6f84,#16404f)" role="img" aria-label="Aquarium tunnel"></div><div class="cat__label">Zoos &amp; Aquariums</div></div>
      <div class="cat cat--active"><div class="cat__img" style="background:linear-gradient(180deg,#8ab8dd,#e9eef3 55%,#2b6f9c)" role="img" aria-label="Cruise ship at sea"><span class="plus">+</span></div><div class="cat__label">Reef &amp; Island Cruises</div></div>
    </div>
    <div class="mascot" style="left:570px;top:255px;width:64px;height:56px" role="img" aria-label="Leaping kangaroo mascot"></div>
  </section>

  <section class="section" style="height:215px">
    <h2 class="reviews-title">What<br>Our Travelers<br>Are Saying</h2>
    <div class="arrows" style="position:absolute;left:96px;top:122px"><span class="arrow arrow--prev"><svg viewBox="0 0 10 6"><path d="M9 3H1M3 1L1 3l2 2" stroke="#a88" fill="none"/></svg></span><span class="arrow" style="background:var(--yellow)"><svg viewBox="0 0 10 6"><path d="M1 3h8M7 1l2 2-2 2" stroke="#222" fill="none"/></svg></span></div>
    <div class="review" style="left:250px;top:42px"><div class="quote">“</div><div class="stars">★★★★★</div><p>Lorem Ipsum is simply dummy text of the printing and typesetting industry. Lorem Ipsum has been the industry's standard dummy text ever since the 1500s.</p><div class="reviewer"><span class="avatar"></span><div><div class="reviewer__name">Marla Denholm</div><div class="reviewer__place">New York, USA</div></div></div></div>
    <div class="review" style="left:407px;top:42px"><div class="quote">“</div><div class="stars">★★★★★</div><p>Lorem Ipsum is simply dummy text of the printing and typesetting industry. Lorem Ipsum has been the industry's standard dummy text ever since the 1500s.</p><div class="reviewer"><span class="avatar"></span><div><div class="reviewer__name">Theo Ranvik</div><div class="reviewer__place">New York, USA</div></div></div></div>
    <div class="mascot mascot--koala" style="left:4px;top:140px;width:54px;height:62px" role="img" aria-label="Koala mascot"></div>
  </section>

  <section class="section section--cream" style="height:310px">
    <h2 class="section__title" style="padding-top:38px">Top New Experience</h2>
    <div class="cards" style="top:66px">
      <div class="card"><div class="card__img" style="background:linear-gradient(160deg,#6aa4d8,#3c6fa8 60%,#9bbf6a)" role="img" aria-label="Theme park visitors on rides"></div><div class="card__body"><div class="badges"><span class="badge badge--hot">Hot deal</span><span class="badge badge--best">Best seller</span></div><p class="card__by">by Zestoria Tickets</p><p class="card__title">Zestoria Park, Wavelark World &amp;<br>Loftpeak 3 Day Ticket</p><div class="card__foot"><div><span class="from">from</span><span class="old">$159.00</span><span class="price">$141.55</span></div><span class="rating">★ 4.7</span></div></div></div>
      <div class="card"><div class="card__img" style="background:linear-gradient(160deg,#f3b15a,#c2552f 55%,#5c7a2f)" role="img" aria-label="Couple watching hot air balloons"></div><div class="card__body"><div class="badges"><span class="badge badge--hot">Hot deal</span><span class="badge badge--best">Best seller</span></div><p class="card__by">by Zestoria Tickets</p><p class="card__title">Zestoria Park, Wavelark World &amp;<br>Loftpeak 3 Day Ticket</p><div class="card__foot"><div><span class="from">from</span><span class="old">$159.00</span><span class="price">$141.55</span></div><span class="rating">★ 4.7</span></div></div></div>
      <div class="card"><div class="card__img" style="background:linear-gradient(160deg,#4f9a3c,#e0b52c 45%,#c8402f 70%,#3d79b8)" role="img" aria-label="Colourful lorikeets feeding"></div><div class="card__body"><div class="badges"><span class="badge badge--hot">Hot deal</span><span class="badge badge--best">Best seller</span></div><p class="card__by">by Zestoria Tickets</p><p class="card__title">Zestoria Park, Wavelark World &amp;<br>Loftpeak 3 Day Ticket</p><div class="card__foot"><div><span class="from">from</span><span class="old">$159.00</span><span class="price">$141.55</span></div><span class="rating">★ 4.7</span></div></div></div>
    </div>
    <div class="progress" style="top:262px"><span class="progress__fill"></span></div>
    <div class="mascot" style="left:566px;top:222px;width:46px;height:76px" role="img" aria-label="Kangaroo mascot"></div>
  </section>

  <footer class="footer">
    <div class="footer__brand">
      <div class="brand"><span class="brand__dot"></span>WANDER-ON TICKETS</div>
      <p class="footer__about">Book tours, attractions and day trips across Australia in minutes, online or from a kiosk right in your hotel lobby. Real local operators, fair prices and friendly help whenever plans change on your trip.</p>
      <div class="footer__label">Sign up for our newsletter</div>
      <div class="newsletter"><span>hello@wanderon-mail.com</span><span class="btn-sub">Subscribe →</span></div>
    </div>
    <div class="footer__col" style="left:290px"><h4>Top Destinations</h4>Saltmarsh Coast Road<br>Redgum Gorge Park<br>Pelican Cove Beach<br>Coralmere<br>Wattlebrook Wildlife Park<br>Quillon Island<br>Ferrycross Bridge<br>Harbourlight Hall<br>Mossvale Gardens<br>Tealwater Reef<br>Emberfield Valley<br>Larkspur Green</div>
    <div class="footer__col" style="left:392px"><h4>Popular Cities</h4>Sydney<br>Melbourne<br>Gold Coast<br>Brisbane<br>Perth<br>Adelaide<br>Hobart<br>Darwin<br>Ballarat<br>Rockhampton<br>Geelong<br>Hervey Bay</div>
    <div class="footer__col" style="left:498px"><h4>Our Company</h4><span class="hl">About Us</span><br>FAQs<br>Blogs<br>Privacy Policy<br>Terms and Conditions<br>Security<h4 style="margin-top:10px">Join Us</h4>Affiliate Partners<br>Experience Operators<br>Careers<br>Let's Collaborate</div>
    <div class="mascot" style="left:2px;top:110px;width:40px;height:80px" role="img" aria-label="Kangaroo mascot"></div>
  </footer>
  <div class="bottom-bar"><span>© 2023 Wander-On. All Right Reserved</span><div class="socials"><span class="social"></span><span class="social social--on"></span><span class="social"></span><span class="social"></span></div></div>
</section>

</body>
</html>
```